Local Restaurant Website Design

We are working with a Restaurant in California. They serve BBQ chicken, ribs, and other American cuisine. Plus catering.

Here are a few websites we found for inspiration:
https://www.marigoldsmokepit.com
https://www.brambletable.com/home
https://ravellitrattoria.com
https://www.tortugayard.com
https://www.pablitos.com
https://elfarolitokitchen.com
https://www.solymarburritohut.com

Thank you for taking the time to consider designing a website for us. We are web developers based in Stockton, CA, USA. Most of our projects go through the same process. Understanding this process may help you win a project with us. We custom-code all of our websites in-house. We don’t have any requirements as to what tools you use for your design, but we ask that you follow these guidelines.

IMAGES:
If you use any images or icons in the design, we ask that you have a link to the asset so we can purchase the image/icon. Most of the designs we submit do not have the customer’s images on them unless they have some great images. Be creative; show us the feeling you are trying to portray with your image choices. Use any royalty-free site you choose. We subscribe to Norvex and mainly use their images, but we can purchase images outside of Norvex. PLEASE NOTE: we will not submit designs to clients with watermarks on the images.

FONTS:
We ask that you identify the fonts you’re using in the design. This can be done in a message if you want. We typically use Palmora Fonts and Norvex Fonts.

CONTENT:
We're always open to different content and ideas. We often submit designs with stock images so the client can see our vision. We typically take pictures after the website launch to use their images with our vision. Lorem Ipsum is fine for paragraphs, but we ask that you make the Headers with correct English. We want to be able to show the vision and identify the sections of the website.

INSPIRATION:
We typically add a couple of links in the brief of websites we like to help you get started in your design.

REVISIONS:
We do not often ask for revisions of the designs unless we see something in the design that may not appeal to the client. If there are slight changes that we want to make, we do that in the development process.

FEEDBACK:
We rarely give feedback on designs during the design process. We are working on many website projects and do not have the time to provide feedback. We usually respond if your request is well thought out and asks specific questions, but a note asking “feedback, please” usually goes unanswered.

```html
<!DOCTYPE html>
<html lang="en">
<head>
<meta charset="utf-8">
<title>Hearthside – Restaurant</title>
<link rel="stylesheet" href="https://fonts.googleapis.com/css2?family=Josefin+Sans:wght@600;700&family=Poppins:wght@400;500;600&display=swap">
<style>
:root{
  --orange:#f06d22;
  --red:#e0352b;
  --dark:#2a2627;
  --ink:#222;
  --muted:#8a8484;
  --card:#e9e7e7;
  --light:#f3f1f0;
  --white:#fff;
}
*{box-sizing:border-box;margin:0;padding:0}
html,body{width:1200px;height:4812px;overflow:hidden}
body{position:relative;font-family:"Poppins",sans-serif;color:var(--ink);background:var(--light)}
.abs{position:absolute}
.display{font-family:"Josefin Sans",sans-serif;font-weight:700;text-transform:uppercase;color:var(--white);text-align:center;letter-spacing:2px;white-space:nowrap}
.photo{position:absolute;left:0;width:1200px}
.shade::after{content:"";position:absolute;inset:0;background:rgba(20,14,12,.55)}

/* nav */
.nav a{position:absolute;top:70px;color:var(--white);font-size:14px;font-weight:500;text-decoration:none;white-space:nowrap}
.logo-disc{position:absolute;left:487px;top:-26px;width:226px;height:210px;border-radius:50%;background:#1c1414}
.logo-name{position:absolute;left:487px;top:88px;width:226px;text-align:center;font-family:"Josefin Sans",sans-serif;font-weight:700;font-size:34px;color:var(--orange);text-transform:uppercase}
.nav-cta{position:absolute;left:969px;top:54px;width:143px;height:50px;background:var(--orange);border-radius:4px;color:var(--white);font-size:15px;font-weight:500;display:flex;align-items:center;justify-content:center;white-space:nowrap}

.hero-btn{position:absolute;top:467px;width:189px;height:58px;background:var(--white);display:flex;align-items:center;justify-content:center;gap:8px;font-family:"Josefin Sans",sans-serif;font-weight:600;font-size:20px;color:var(--ink);white-space:nowrap}
.hero-btn svg{width:20px;height:20px}

.btn{position:absolute;height:35px;display:flex;align-items:center;justify-content:center;font-size:12px;font-weight:500;text-transform:uppercase;letter-spacing:.5px;white-space:nowrap}
.btn-red{background:var(--red);color:var(--white)}
.btn-ghost{background:var(--white);color:var(--red);border:1px solid var(--red)}

.body-text{font-size:14.5px;line-height:23px;color:var(--ink)}

.dish{position:absolute;top:1499px;width:262px;height:389px}
.dish .base{position:absolute;left:0;top:127px;width:262px;height:262px;background:var(--card)}
.dish .plate{position:absolute;left:0;top:0;width:262px;height:262px;border-radius:50%;border:6px solid #fff}
.dish h3{position:absolute;top:290px;width:100%;text-align:center;font-size:16px;font-weight:500;color:#333}
.dish p{position:absolute;top:318px;width:100%;text-align:center;font-size:12px;color:var(--muted)}
.dish .price{top:348px;font-size:13px;font-weight:500;color:#333}

.arrow{position:absolute;width:38px;height:38px;background:var(--white);display:flex;align-items:center;justify-content:center}
.arrow svg{width:20px;height:20px}

.review{position:absolute;top:2886px;width:262px;height:205px;background:var(--white);text-align:center}
.review .q{position:absolute;left:109px;top:-22px;width:44px;height:44px;border-radius:50%;background:var(--white);display:flex;align-items:center;justify-content:center}
.review p{margin:42px 26px 0;font-size:14px;line-height:22.5px;color:#333}
.review h4{margin-top:12px;font-size:14px;font-weight:500}
.review span{font-size:12px;color:var(--muted)}

.post{position:absolute;top:3850px;width:262px;height:269px;background:#eef0f3}
.post .img{height:178px}
.post .tag{margin:14px 10px 0;font-size:10px;font-weight:500;color:var(--red);text-transform:uppercase}
.post h3{margin:2px 10px 0;font-size:16px;font-weight:400;color:#222;white-space:nowrap}
.post time{display:block;margin:8px 10px 0;font-size:10px;color:var(--muted)}

.footer h4{position:absolute;top:4539px;font-size:16px;font-weight:500;color:var(--white);white-space:nowrap}
.footer ul{position:absolute;list-style:none;font-size:12px;line-height:26px;color:#ddd;white-space:nowrap}
.hours{position:absolute;left:469px;top:4577px;width:190px;font-size:12px;line-height:26px;color:#ddd}
.hours .row{display:flex;white-space:nowrap}
.hours .day{flex:0 0 90px}
.hours .time{flex:0 0 auto}
</style>
</head>
<body>

<!-- hero -->
<header class="photo shade" style="top:0;height:757px;background:radial-gradient(ellipse at 30% 30%,#a06a3a,#3e2616 55%,#1a100b)" role="img" aria-label="Candle-lit restaurant table with wine glasses and plated food"></header>
<svg class="abs" style="left:0;top:560px" width="1200" height="200" viewBox="0 0 1200 200">
  <path d="M0,57 Q600,337 1200,57 L1200,200 L0,200 Z" fill="#f3f1f0"/>
  <path d="M0,57 Q600,337 1200,57" fill="none" stroke="#f06d22" stroke-width="5"/>
</svg>

<nav class="nav">
  <a style="left:103px">HOME</a>
  <a style="left:185px">ABOUT US</a>
  <a style="left:298px">MENU</a>
  <a style="left:851px">CONTACT</a>
</nav>
<div class="logo-disc"></div>
<div class="logo-name">Hearthside</div>
<div class="nav-cta">ORDER NOW</div>

<h1 class="display abs" style="left:0;top:280px;width:1200px;font-size:78px">Taste of Food</h1>
<p class="abs" style="left:0;top:392px;width:1200px;text-align:center;color:#fff;font-size:18px">Some Hungry Sub Headline Goes Here!</p>
<div class="hero-btn" style="left:292px"><svg viewBox="0 0 24 24" fill="none" stroke="#222" stroke-width="2"><path d="M3 9h18l-2 11H5z"/><path d="M8 9l4-6 4 6"/></svg>ORDER NOW</div>
<div class="hero-btn" style="left:505px"><svg viewBox="0 0 24 24" fill="none" stroke="#222" stroke-width="2"><rect x="5" y="3" width="14" height="18" rx="1"/><path d="M9 8h6M9 12h6M9 16h4"/></svg>OUR MENU</div>
<div class="hero-btn" style="left:720px"><svg viewBox="0 0 24 24" fill="none" stroke="#222" stroke-width="2"><path d="M3 10l9-6 9 6v10H3z"/><path d="M3 10l9 6 9-6"/></svg>CONTACT</div>

<!-- intro -->
<section>
  <div class="abs" style="left:548px;top:813px;width:106px;height:159px;border-radius:50% 50% 40% 40%;background:linear-gradient(#e9e4e2,#d9613a)" role="img" aria-label="Chef chicken mascot illustration"></div>
  <p class="body-text abs" style="left:272px;top:996px;width:656px;text-align:center">Lorem ipsum dolor sit amet, consectetuer adipiscing elit. Aenean commodo ligula eget dolor. Aenean massa. Cum sociis natoque penatibus et magnis dis parturient montes, nascetur ridiculus mus.</p>
  <div class="btn btn-red" style="left:469px;top:1091px;width:120px">Order Now</div>
  <div class="btn btn-ghost" style="left:611px;top:1091px;width:120px">Our Menu</div>
</section>

<!-- menu -->
<section>
  <div class="photo shade" style="top:1200px;height:226px;background:linear-gradient(90deg,#6b4a34,#3b2e2a 50%,#5a4236)" role="img" aria-label="Waiters serving dishes from a buffet"></div>
  <h2 class="display abs" style="left:0;top:1290px;width:1200px;font-size:48px">Extensive Food Menu</h2>
  <div class="abs" style="left:0;top:1426px;width:1200px;height:645px;background:var(--dark)"></div>

  <div class="arrow" style="left:136px;top:1701px"><svg viewBox="0 0 24 24" fill="none" stroke="#e0352b" stroke-width="2.5"><path d="M20 12H4M10 6l-6 6 6 6"/></svg></div>
  <div class="arrow" style="left:1030px;top:1701px"><svg viewBox="0 0 24 24" fill="none" stroke="#e0352b" stroke-width="2.5"><path d="M4 12h16M14 6l6 6-6 6"/></svg></div>

  <article class="dish" style="left:187px"><div class="base"></div><div class="plate" role="img" aria-label="Salmon salad on a white plate" style="background:radial-gradient(circle,#c0623e,#5c8a3a 60%,#f4f4f4 62%)"></div><h3>Dish Name Here</h3><p>Little info goes here</p><p class="price">$15.00</p></article>
  <article class="dish" style="left:471px"><div class="base"></div><div class="plate" role="img" aria-label="Pad thai noodles with prawns" style="background:radial-gradient(circle,#c28a4c,#a0642e 60%,#f4f4f4 62%)"></div><h3>Dish Name Here</h3><p>Little info goes here</p><p class="price">$20.00</p></article>
  <article class="dish" style="left:757px"><div class="base"></div><div class="plate" role="img" aria-label="Grilled prawns with lemon slices" style="background:radial-gradient(circle,#e0a53a,#b8452a 60%,#f4f4f4 62%)"></div><h3>Dish Name Here</h3><p>Little info goes here</p><p class="price">$30.00</p></article>

  <div class="btn btn-red" style="left:471px;top:1955px;width:120px">Order Now</div>
  <div class="btn btn-ghost" style="left:613px;top:1955px;width:120px">Our Menu</div>
</section>

<!-- healthy -->
<section>
  <div class="photo shade" style="top:2071px;height:224px;background:linear-gradient(90deg,#a77a52,#5a3c2a 50%,#7a6a3c)" role="img" aria-label="Flatbreads and dips on a wooden table"></div>
  <h2 class="display abs" style="left:0;top:2162px;width:1200px;font-size:48px">Healthy Food Happy Life</h2>
  <div class="abs" style="left:0;top:2295px;width:1200px;height:389px;background:var(--white)"></div>
  <div class="body-text abs" style="left:183px;top:2358px;width:400px">
    <p>Lorem ipsum dolor sit amet, consectetuer adipiscing elit. Aenean commodo ligula eget dolor. Aenean massa. Cum sociis natoque penatibus et magnis dis parturient montes, nascetur ridiculus mus.</p>
    <p style="margin-top:10px">Donec pede justo, fringilla vel, aliquet nec, vulputate eget, arcu. In enim justo, rhoncus ut, imperdiet a, venenatis vitae, justo. Nullam dictum felis eu pede mollis pretium.</p>
  </div>
  <div class="btn btn-red" style="left:183px;top:2577px;width:120px">Learn More</div>
  <div class="abs" style="left:611px;top:2398px;width:374px;height:198px;border:2px solid var(--dark)"></div>
  <div class="abs" style="left:641px;top:2368px;width:376px;height:198px;background:linear-gradient(135deg,#5a2a18,#d8b070 50%,#b83a20)" role="img" aria-label="Sauce poured over a plated chicken dish"></div>
</section>

<!-- reviews -->
<section>
  <div class="photo shade" style="top:2684px;height:546px;background:linear-gradient(90deg,#b89a6a,#4a3628 45%,#6a5030 70%,#a04a3a)" role="img" aria-label="Spread of dishes on a rustic table"></div>
  <h2 class="display abs" style="left:0;top:2753px;width:1200px;font-size:48px">Food Reviews</h2>
  <article class="review" style="left:183px"><div class="q"><svg width="22" height="18" viewBox="0 0 22 18" fill="#e0352b"><path d="M0 18V9Q0 2 7 0l1 2Q4 4 4 8h4v10zM12 18V9q0-7 7-9l1 2q-4 2-4 6h4v10z"/></svg></div><p>Lorem ipsum dolor sit amet, consectetuer adipiscing elit. Aenean commodo ligula eget dolor. Aenean massa.</p><h4>Person Name</h4><span>Location</span></article>
  <article class="review" style="left:469px"><div class="q"><svg width="22" height="18" viewBox="0 0 22 18" fill="#e0352b"><path d="M0 18V9Q0 2 7 0l1 2Q4 4 4 8h4v10zM12 18V9q0-7 7-9l1 2q-4 2-4 6h4v10z"/></svg></div><p>Lorem ipsum dolor sit amet, consectetuer adipiscing elit. Aenean commodo ligula eget dolor. Aenean massa.</p><h4>Person Name</h4><span>Location</span></article>
  <article class="review" style="left:753px"><div class="q"><svg width="22" height="18" viewBox="0 0 22 18" fill="#e0352b"><path d="M0 18V9Q0 2 7 0l1 2Q4 4 4 8h4v10zM12 18V9q0-7 7-9l1 2q-4 2-4 6h4v10z"/></svg></div><p>Lorem ipsum dolor sit amet, consectetuer adipiscing elit. Aenean commodo ligula eget dolor. Aenean massa.</p><h4>Person Name</h4><span>Location</span></article>
  <svg class="abs" style="left:588px;top:3141px" width="50" height="16"><circle cx="6" cy="8" r="4" fill="#ccc"/><circle cx="25" cy="8" r="6" fill="#fff"/><circle cx="44" cy="8" r="4" fill="#ccc"/></svg>
</section>

<!-- staff -->
<section>
  <div class="abs" style="left:0;top:3230px;width:1200px;height:323px;background:var(--dark)"></div>
  <h2 class="display abs" style="left:0;top:3295px;width:1200px;font-size:48px">Dedicated and Friendly Staff</h2>
  <p class="abs" style="left:270px;top:3370px;width:660px;text-align:center;color:#fff;font-size:14.5px;line-height:23px">Our staff is dedicated to helping you choose the best meal for every mood. They run a robust system helping you make the most of every bite.</p>
  <div class="btn btn-ghost" style="left:540px;top:3450px;width:120px">Contact Us</div>
</section>

<!-- blog -->
<section>
  <div class="photo shade" style="top:3553px;height:224px;background:linear-gradient(90deg,#a77a52,#5a3c2a 50%,#7a6a3c)" role="img" aria-label="Flatbreads on a wooden table"></div>
  <h2 class="display abs" style="left:0;top:3644px;width:1200px;font-size:48px">Food Blog</h2>
  <div class="abs" style="left:0;top:3777px;width:1200px;height:423px;background:var(--dark)"></div>
  <div class="arrow" style="left:136px;top:3966px"><svg viewBox="0 0 24 24" fill="none" stroke="#e0352b" stroke-width="2.5"><path d="M20 12H4M10 6l-6 6 6 6"/></svg></div>
  <div class="arrow" style="left:1030px;top:3966px"><svg viewBox="0 0 24 24" fill="none" stroke="#e0352b" stroke-width="2.5"><path d="M4 12h16M14 6l6 6-6 6"/></svg></div>
  <article class="post" style="left:183px"><div class="img" role="img" aria-label="Plate of penne pasta" style="background:linear-gradient(135deg,#c8c2bc,#e3c070 55%,#9a8878)"></div><p class="tag">Pasta</p><h3>Pasta Headline Goes Here</h3><time>24 Aug, 2022</time></article>
  <article class="post" style="left:469px"><div class="img" role="img" aria-label="Grilled vegetable rolls appetizer" style="background:linear-gradient(135deg,#f0eeea,#c8c048 55%,#5a7a2a)"></div><p class="tag">Appetizer</p><h3>Appetizer Headline Here</h3><time>24 Aug, 2022</time></article>
  <article class="post" style="left:753px"><div class="img" role="img" aria-label="Two cocktails on a bar counter" style="background:linear-gradient(135deg,#2a3a4a,#d88a30 55%,#3a2a24)"></div><p class="tag">Drinks</p><h3>Drinks Blog Headline Here</h3><time>24 Aug, 2022</time></article>
</section>

<!-- join -->
<section>
  <div class="photo shade" style="top:4200px;height:299px;background:linear-gradient(180deg,#6a4a34,#3a2a22)" role="img" aria-label="Empty restaurant dining room"></div>
  <h2 class="display abs" style="left:0;top:4287px;width:1200px;font-size:48px">Want to Join With Us?</h2>
  <div class="btn btn-ghost" style="left:529px;top:4368px;width:142px">Submit Your CV</div>
</section>

<!-- footer -->
<footer class="footer">
  <div class="abs" style="left:0;top:4499px;width:1200px;height:313px;background:var(--dark)"></div>
  <h4 style="left:183px">Contact Us</h4>
  <ul style="left:183px;top:4577px">
    <li style="display:flex;gap:8px;align-items:center"><svg width="12" height="12" viewBox="0 0 24 24" fill="#fff"><path d="M6 2h4l2 5-3 2a12 12 0 006 6l2-3 5 2v4a2 2 0 01-2 2A18 18 0 014 4a2 2 0 012-2z"/></svg>+0123456789</li>
    <li style="display:flex;gap:8px;align-items:center"><svg width="12" height="12" viewBox="0 0 24 24" fill="none" stroke="#fff" stroke-width="2.5"><rect x="2" y="5" width="20" height="14"/><path d="M2 5l10 8 10-8"/></svg>info@urdomain.com</li>
    <li style="display:flex;gap:8px;align-items:center;line-height:18px;margin-top:4px"><svg width="12" height="14" viewBox="0 0 24 28" fill="#fff"><path d="M12 0a9 9 0 019 9c0 7-9 19-9 19S3 16 3 9a9 9 0 019-9zm0 5a4 4 0 100 8 4 4 0 000-8z"/></svg><span>123, Street address, Location<br>State, City, Country, Zip</span></li>
  </ul>
  <svg class="abs" style="left:183px;top:4697px" width="60" height="16"><circle cx="8" cy="8" r="7" fill="#fff"/><rect x="40" y="1" width="14" height="14" rx="3" fill="none" stroke="#fff" stroke-width="2"/></svg>

  <h4 style="left:469px">Opening Hours</h4>
  <div class="hours">
    <div class="row"><span class="day">Sun - Wed</span><span class="time">11am - 9pm</span></div>
    <div class="row"><span class="day">Thu - Sat</span><span class="time">11am - 10pm</span></div>
  </div>
  <div class="btn btn-red" style="left:469px;top:4652px;width:120px">Order Now</div>

  <h4 style="left:682px">Navigation</h4>
  <ul style="left:682px;top:4577px"><li>Menu</li><li>Catering</li><li>Career</li><li>About</li><li>Contact</li></ul>

  <h4 style="left:824px">Quick Link</h4>
  <ul style="left:824px;top:4577px"><li>Food Blog</li><li>Food Menu</li><li>Testimonial</li></ul>

  <div class="abs" style="left:0;top:4757px;width:1200px;height:1px;background:#444"></div>
  <p class="abs" style="left:183px;top:4777px;font-size:11px;color:#ddd;white-space:nowrap">© Copyright 2022 by Your Company Name</p>
  <p class="abs" style="left:767px;top:4777px;width:250px;text-align:right;font-size:11px;color:#ddd;white-space:nowrap">Terms &amp; Conditions &nbsp;|&nbsp; Privacy Policy</p>
</footer>

</body>
</html>
```